Post card for annual skin cancer screening exam

We are looking to design a modern, classy, clean, but fun postcard that we will send out to patients to remind them to schedule their follow up exams for our dermatology office.

It should include our logo
http://tovimek.com/design/logo/jpg/tovimek2.jpg
http://tovimek.com/design/logo/jpg/tovimek.jpg

Address
Phone number
website

We are open to your ideas on wording, as something clever is always appreciated - though this is going to both young and elderly patients - so the message must be easy to read and clear.
Updates

Font styles to use
Serif

Colors
85cae6
3176b5

Requirements
Must have
• Logo
• Office address
• Phone number
• website
• call to action message - to schedule a follow up visit

```html
<!DOCTYPE html>
<html lang="en">
<head>
<meta charset="utf-8">
<title>Tovimek Dermatology – Screening Reminder Postcard</title>
<link href="https://fonts.googleapis.com/css2?family=Open+Sans:ital,wght@0,400;0,600;0,700;1,600&display=swap" rel="stylesheet">
<style>
  :root{
    --page:#eceff1;
    --sky:#e2f2f8;
    --sky-pale:#d9eeee;
    --brand-light:#85cae6;
    --brand:#3176b5;
    --brand-deep:#1f6aa6;
    --ink:#4a4f55;
    --ink-soft:#6a6f74;
    --rule:#9aa3aa;
    --white:#ffffff;
  }
  *{box-sizing:border-box;margin:0;padding:0}
  html,body{width:877px;height:1200px;overflow:hidden;background:var(--page)}
  body{position:relative;font-family:"Open Sans",Arial,sans-serif;color:var(--ink)}

  .postcard{position:absolute;background:var(--white);box-shadow:0 4px 14px rgba(0,0,0,.22);overflow:hidden}
  .postcard svg.shapes{position:absolute;inset:0;width:100%;height:100%}

  /* front */
  .front{left:57px;top:46px;width:682px;height:526px;background:var(--sky)}
  .front__title{position:absolute;left:40px;top:24px;font-size:23px;font-weight:700;color:var(--brand-deep);letter-spacing:.2px}
  .front__badge{position:absolute;left:502px;top:270px;width:146px;height:146px;border-radius:50%;
    background:var(--white);border:5px solid #d3e6ef;box-shadow:0 3px 8px rgba(0,0,0,.3);
    display:flex;align-items:center;justify-content:center;text-align:center}
  .brand-name{font-size:20px;font-weight:600;color:var(--brand);line-height:1.15}
  .front__cta{position:absolute;left:16px;top:476px;font-size:20px;font-style:italic;font-weight:600;color:var(--ink-soft)}
  .front__web{position:absolute;right:24px;top:446px;font-size:22px;font-weight:700;color:var(--brand-deep)}
  .front__phone{position:absolute;right:24px;top:478px;font-size:19px;font-weight:700;color:var(--ink-soft);display:flex;align-items:center;gap:6px}
  .phone-icon{width:20px;height:20px}

  /* back */
  .back{left:137px;top:626px;width:679px;height:526px}
  .back__slogan{position:absolute;left:27px;top:100px;font-size:19px;font-weight:600;color:var(--brand-deep);line-height:1.3}
  .back__brand{position:absolute;left:60px;top:220px;width:240px;text-align:center}
  .back__message{position:absolute;left:18px;top:308px;width:300px;text-align:center;font-size:14px;line-height:1.45;color:var(--ink)}
  .back__message em{display:block;margin-top:12px}
  .back__web{position:absolute;left:18px;top:424px;width:300px;text-align:center;font-size:22px;font-weight:700;color:var(--brand-deep)}
  .back__phone{position:absolute;left:18px;top:460px;width:300px;justify-content:center;font-size:17px;font-weight:700;color:var(--ink-soft);display:flex;align-items:center;gap:6px}
  .back__return{position:absolute;left:385px;top:22px;font-size:11px;line-height:1.55;color:#333}
  .stamp-box{position:absolute;left:564px;top:28px;width:95px;height:74px;border:1.5px solid #b9c0c5}
  .address-line{position:absolute;left:432px;width:227px;height:0;border-top:1.2px solid var(--rule)}
</style>
</head>
<body>

<section class="postcard front" aria-label="Postcard front">
  <svg class="shapes" viewBox="0 0 682 526" aria-hidden="false">
    <defs>
      <linearGradient id="exam-photo-tones" x1="0" y1="0" x2="1" y2="0">
        <stop offset="0" stop-color="#b8a59a"/>
        <stop offset=".35" stop-color="#e6d6c8"/>
        <stop offset=".7" stop-color="#eeeae6"/>
        <stop offset="1" stop-color="#dcdfe2"/>
      </linearGradient>
    </defs>
    <path d="M0 82 Q330 52 682 88 L682 0 L0 0 Z" fill="var(--sky)"/>
    <path role="img" aria-label="Photo: a dermatologist examining a smiling patient's cheek in a clinic"
          d="M0 80 Q330 48 682 86 L682 330 Q420 440 0 380 Z" fill="url(#exam-photo-tones)"/>
    <path d="M0 72 Q330 40 682 80 L682 88 Q330 58 0 84 Z" fill="var(--brand)"/>
    <path d="M0 380 Q420 440 682 330 L682 346 Q430 470 0 404 Z" fill="var(--brand-light)"/>
    <path d="M0 392 Q420 456 682 338 L682 344 Q430 466 0 400 Z" fill="var(--brand)"/>
  </svg>
  <h1 class="front__title">REMINDER: ANNUAL SKIN CANCER SCREENING EXAM</h1>
  <div class="front__badge"><span class="brand-name">Tovimek<br>Dermatology</span></div>
  <p class="front__cta">Schedule Your Exam</p>
  <p class="front__web">www.tovimek.com</p>
  <p class="front__phone">
    <svg class="phone-icon" viewBox="0 0 24 24" aria-hidden="true"><circle cx="12" cy="12" r="10.5" fill="none" stroke="currentColor" stroke-width="2"/><path d="M8.2 6.5l2 2.2-1.2 1.6c.8 1.8 2 3 3.8 3.8l1.6-1.2 2.2 2-1.2 1.8c-3.8-.5-7.2-3.9-7.7-7.7z" fill="currentColor"/></svg>
    (555) 010-7546 (SKIN)
  </p>
</section>

<section class="postcard back" aria-label="Postcard back">
  <svg class="shapes" viewBox="0 0 679 526">
    <defs>
      <linearGradient id="water-tones" x1="0" y1="0" x2="0" y2="1">
        <stop offset="0" stop-color="#ffffff"/>
        <stop offset=".45" stop-color="#e4f1f7"/>
        <stop offset="1" stop-color="#a9d3e6"/>
      </linearGradient>
      <clipPath id="left-panel"><path d="M0 0 H300 Q470 263 325 526 H0 Z"/></clipPath>
    </defs>
    <g clip-path="url(#left-panel)">
      <rect role="img" aria-label="Photo: clear water with rising bubbles" x="0" y="0" width="420" height="186" fill="url(#water-tones)"/>
      <rect x="0" y="186" width="420" height="92" fill="var(--white)"/>
      <rect x="0" y="278" width="420" height="248" fill="var(--sky-pale)"/>
    </g>
    <path d="M300 0 Q470 263 325 526 L352 526 Q505 263 318 0 Z" fill="var(--brand-light)"/>
    <path d="M310 0 Q485 263 338 526 L346 526 Q496 263 316 0 Z" fill="var(--brand)"/>
  </svg>
  <p class="back__slogan">BE GOOD<br>TO YOUR SKIN</p>
  <p class="back__brand"><span class="brand-name">Tovimek Dermatology</span></p>
  <p class="back__message">We offer a wide variety of information to help you learn about your skin condition from a source you can trust.
    <em>Schedule a consultation, and take the first step toward looking and feeling your best.</em></p>
  <p class="back__web">www.tovimek.com</p>
  <p class="back__phone">
    <svg class="phone-icon" viewBox="0 0 24 24" aria-hidden="true"><circle cx="12" cy="12" r="10.5" fill="none" stroke="currentColor" stroke-width="2"/><path d="M8.2 6.5l2 2.2-1.2 1.6c.8 1.8 2 3 3.8 3.8l1.6-1.2 2.2 2-1.2 1.8c-3.8-.5-7.2-3.9-7.7-7.7z" fill="currentColor"/></svg>
    (555) 010-7546 (SKIN)
  </p>
  <address class="back__return" style="font-style:normal">Tovimek Dermatology<br>412 Meadow Brook Road;<br>Fairhaven NY 11990</address>
  <div class="stamp-box"></div>
  <div class="address-line" style="top:230px"></div>
  <div class="address-line" style="top:273px"></div>
  <div class="address-line" style="top:316px"></div>
  <div class="address-line" style="top:360px"></div>
</section>

</body>
</html>
```